Florida-based Coastal Landscaping Comapny Needs Postcard Designs

We are a newly established Florida-based, coastal landscaping company that is looking for some really innovative postcards that we can use to get our name our to affluent consumers that live on the coast of Florida (think on the beach) and small to medium sized businesses in the same area. We will be sending out 100s of thousands of these, so need a great design

Target Market(s)

Affluent consumers and small to medium sized businesses

Industry/Entity Type

Landscaping

Font styles to use
Sans Serif

Colors

Designer to choose colors to be used in the design.

Requirements
Must have
• Florida - looking, island looking / paradise, but incorporate landscaping themes
• Need to say something about "Enjoy your yard this summer" or something relating to summer, landscapes and florida
• and would like to make two offers $50.00 off with signing up for one of our routine maintenance programs, or 1 free landscape inspection
Should not have
• Regular generic lawn company designs. We are a top tier landscape design / build plus maintenance firm, so not your mom and pop lawn mowing company

```html
<!DOCTYPE html>
<html lang="en">
<head>
<meta charset="utf-8">
<title>Shorewell Coastal Landscaping Postcard</title>
<link rel="stylesheet" href="https://fonts.googleapis.com/css2?family=Roboto+Condensed:wght@400;700&family=Kaushan+Script&family=Archivo+Black&display=swap">
<style>
  :root {
    --page: #ffffff;
    --ocean-deep: #2b7ca3;
    --ocean: #31a9d8;
    --ocean-light: #58c3ea;
    --foam: #ffffff;
    --sky-top: #c4d8ee;
    --sky-low: #e9eff6;
    --garden: #6e8a4a;
    --garden-deep: #4d6e36;
    --bloom: #b8586a;
    --title-blue: #3aa6ef;
    --ribbon: #c8222c;
    --dash: #ffffff;
  }
  * { box-sizing: border-box; margin: 0; padding: 0; }
  html, body {
    width: 789px; height: 1200px; overflow: hidden;
    background: var(--page);
    font-family: "Roboto Condensed", "Arial Narrow", sans-serif;
  }
  .canvas { position: relative; width: 789px; height: 1200px; }
  .card {
    position: absolute; left: 44px; width: 700px; height: 545px;
    overflow: hidden; background: var(--foam);
  }
  .card--front { top: 40px; }
  .card--back { top: 615px; border: 1px solid #d8d8d8; }
  .card__art { position: absolute; inset: 0; width: 100%; height: 100%; }
  .card__text { position: absolute; color: var(--foam); white-space: nowrap; }

  .headline {
    left: 0; right: 0; top: 20px; text-align: center;
    font-family: "Kaushan Script", cursive; font-weight: 400; font-size: 43px;
    color: var(--title-blue);
    text-shadow: 0 0 4px #fff, 0 0 8px #fff, 0 0 12px #fff;
  }
  .brand-name {
    font-family: "Roboto Condensed", sans-serif; font-weight: 700;
    font-size: 38px; letter-spacing: 2px; color: var(--foam);
    display: flex; align-items: center; gap: 10px;
  }
  .brand-name__dot { width: 14px; height: 14px; border-radius: 50%; background: var(--foam); }
  .front-brand { left: 28px; top: 398px; }
  .specialty { left: 290px; top: 396px; font-weight: 700; font-size: 25px; }
  .services { left: 290px; top: 436px; font-size: 22px; letter-spacing: .3px; }
  .estimate { left: 30px; top: 488px; font-family: "Kaushan Script", cursive; font-size: 22px; }
  .contact { display: flex; align-items: center; gap: 6px; }
  .contact svg { fill: var(--foam); flex: none; }
  .front-phone { left: 298px; top: 490px; font-weight: 700; font-size: 22px; }
  .front-web { left: 462px; top: 494px; font-size: 16px; }

  .back-brand { left: 38px; top: 50px; }
  .back-phone { left: 0; width: 290px; justify-content: center; top: 132px; font-weight: 700; font-size: 21px; }
  .back-web { left: 0; width: 290px; justify-content: center; top: 160px; font-size: 16px; }
  .coupon {
    position: absolute; left: 38px; width: 213px;
    border: 2px dashed var(--dash); color: var(--foam); text-align: center;
  }
  .coupon--discount { top: 209px; height: 109px; padding-top: 20px; }
  .coupon--inspection { top: 338px; height: 97px; padding-top: 18px; }
  .coupon__headline { font-family: "Archivo Black", sans-serif; font-size: 24px; line-height: 1.1; }
  .coupon__detail { font-weight: 700; font-size: 14px; line-height: 1.35; }
  .coupon__detail--caps { font-size: 16px; }
  .coupon__ribbon { position: absolute; left: -3px; top: -3px; width: 62px; height: 62px; }
  .coupon__ribbon-text {
    position: absolute; left: 4px; top: 11px; transform: rotate(-45deg);
    font-size: 8px; font-weight: 700; line-height: 1; text-align: center; color: var(--foam);
  }
  .tagline {
    left: 0; width: 290px; top: 468px; text-align: center; white-space: normal;
    font-family: "Kaushan Script", cursive; font-size: 22px; line-height: 1.35;
  }
</style>
</head>
<body>
<main class="canvas">

  <section class="card card--front" aria-label="Postcard front">
    <svg class="card__art" viewBox="0 0 700 545">
      <defs>
        <linearGradient id="scene-tones" x1="0" y1="0" x2="0" y2="1">
          <stop offset="0" stop-color="var(--sky-top)"/>
          <stop offset=".3" stop-color="var(--sky-low)"/>
          <stop offset=".62" stop-color="var(--garden)"/>
          <stop offset=".85" stop-color="var(--garden-deep)"/>
          <stop offset="1" stop-color="var(--bloom)"/>
        </linearGradient>
        <linearGradient id="front-sea" x1="0" y1="0" x2="1" y2="0">
          <stop offset="0" stop-color="var(--ocean-deep)"/>
          <stop offset=".55" stop-color="var(--ocean)"/>
          <stop offset="1" stop-color="var(--ocean)"/>
        </linearGradient>
      </defs>
      <rect class="photo-area" width="700" height="380" fill="url(#scene-tones)" role="img"
            aria-label="Photo of a pink stucco Florida home with tall palm trees and beds of red and pink flowers"/>
      <path d="M0 245 Q240 390 700 340 L700 545 L0 545 Z" fill="var(--foam)"/>
      <path d="M0 285 Q260 410 700 355 L700 545 L0 545 Z" fill="var(--ocean-light)"/>
      <path d="M0 315 Q300 420 700 372 L700 545 L0 545 Z" fill="url(#front-sea)"/>
    </svg>
    <h1 class="card__text headline">Sit back and enjoy your summer!</h1>
    <div class="card__text brand-name front-brand"><span class="brand-name__dot"></span>SHOREWELL</div>
    <p class="card__text specialty">COASTAL LANDSCAPING SPECIALISTS</p>
    <p class="card__text services">DESIGN ★ INSTALLATION ★ MAINTENANCE</p>
    <p class="card__text estimate">Call for a free estimate!</p>
    <p class="card__text contact front-phone">
      <svg width="14" height="18" viewBox="0 0 14 18"><path d="M3 1 L6 1 L7 5 L5 6.5 Q6 10 8.5 12.5 L10 11 L13 13 L13 16 Q11 17.5 8 16 Q2 12 1 5 Q1 2 3 1Z"/></svg>
      555-218-4076</p>
    <p class="card__text contact front-web">
      <svg width="15" height="15" viewBox="0 0 16 16"><path fill="none" stroke="#fff" stroke-width="1.4" d="M8 1a7 7 0 1 0 0 14A7 7 0 1 0 8 1ZM1 8h14M8 1c-3 3-3 11 0 14M8 1c3 3 3 11 0 14M2.5 4.5h11M2.5 11.5h11"/></svg>
      www.shorewellcoastal.com</p>
  </section>

  <section class="card card--back" aria-label="Postcard back">
    <svg class="card__art" viewBox="0 0 700 545">
      <defs>
        <linearGradient id="back-sea" x1="0" y1="0" x2="0" y2="1">
          <stop offset="0" stop-color="var(--ocean-deep)"/>
          <stop offset=".6" stop-color="var(--ocean)"/>
          <stop offset="1" stop-color="var(--ocean)"/>
        </linearGradient>
      </defs>
      <path d="M0 0 L468 0 Q320 230 386 545 L0 545 Z" fill="var(--ocean)"/>
      <path d="M0 0 L430 0 Q290 220 347 545 L0 545 Z" fill="url(#back-sea)"/>
    </svg>
    <div class="card__text brand-name back-brand"><span class="brand-name__dot"></span>SHOREWELL</div>
    <p class="card__text contact back-phone">
      <svg width="13" height="17" viewBox="0 0 14 18"><path d="M3 1 L6 1 L7 5 L5 6.5 Q6 10 8.5 12.5 L10 11 L13 13 L13 16 Q11 17.5 8 16 Q2 12 1 5 Q1 2 3 1Z"/></svg>
      555-218-4076</p>
    <p class="card__text contact back-web">
      <svg width="14" height="14" viewBox="0 0 16 16"><path fill="none" stroke="#fff" stroke-width="1.4" d="M8 1a7 7 0 1 0 0 14A7 7 0 1 0 8 1ZM1 8h14M8 1c-3 3-3 11 0 14M8 1c3 3 3 11 0 14M2.5 4.5h11M2.5 11.5h11"/></svg>
      www.shorewellcoastal.com</p>

    <div class="coupon coupon--discount">
      <svg class="coupon__ribbon" viewBox="0 0 62 62"><path d="M0 38 L38 0 L62 0 L0 62 Z" fill="var(--ribbon)"/></svg>
      <span class="coupon__ribbon-text">Special<br>OFFER</span>
      <p class="coupon__headline">$50.00 off</p>
      <p class="coupon__detail">When you sign up for one of<br>our maintenance programs.</p>
    </div>

    <div class="coupon coupon--inspection">
      <svg class="coupon__ribbon" viewBox="0 0 62 62"><path d="M0 38 L38 0 L62 0 L0 62 Z" fill="var(--ribbon)"/></svg>
      <span class="coupon__ribbon-text">Special<br>OFFER</span>
      <p class="coupon__headline">FREE</p>
      <p class="coupon__detail coupon__detail--caps">LANDSCAPE INSPECTION</p>
    </div>

    <p class="card__text tagline">Call us for all your<br>landscaping needs!</p>
  </section>

</main>
</body>
</html>
```